Brightvale, The Pixel Nest or Coding for Kids

Brightvale
We build talent
We need a creative inspiring poster design for a new company based in Bahrain called 'Brightvale'. we teach children computer coding (game developments) and robotics in a play like environment. (activity-based not lectured based) which will develop kids talents in a challenging and enjoying way. (serious and fun)

we like and eye catching poster that will inspire kids to join our academy. Use vibrant color to create energy, elicit a mood and attract the eye.
The poster should be based on our value of:
Inspiration
learning is fun
knowledge is power

Relevant ideas were written on the image I attached.
Updates

Target Market(s)

Parents and KIds

Industry/Entity Type

Education

Logo Text

Brightvale, Building Talents

Font styles to use
Sans Serif

Colors
ec1f27
f37122
f78f20
ffc214
fbef40
9bcb3c
add136
33b8a4
33a6d7

Requirements
Must have
• looking for a design that when a parent see it: "I want to get my kid in to coding!"
• attractive,elegant,colorful,inspiring with a simple and strong message.

```html
<!DOCTYPE html>
<html lang="en">
<head>
<meta charset="utf-8">
<title>Brightvale — Page</title>
<link rel="stylesheet" href="https://fonts.googleapis.com/css2?family=Arimo:wght@400;700&family=Fira+Sans:ital,wght@1,700&display=swap">
<style>
:root{
  --bar-blue:#435f9c;
  --bar-blue-dark:#3b5491;
  --notice-blue:#6e86b6;
  --page-bg:#e9eaed;
  --card:#ffffff;
  --card-line:#dddfe2;
  --soft:#f6f7f9;
  --text:#1d2129;
  --muted:#4b4f56;
  --faint:#90949c;
  --link:#365899;
  --brand-teal:#2b5f6c;
  --cover-text:#1f6c78;
  --avatar:#c5cee0;
  --button-blue:#4e69a2;
}
*{box-sizing:border-box;margin:0;padding:0}
html,body{width:1200px;height:893px;overflow:hidden;background:var(--page-bg)}
body{font-family:'Arimo',Arial,sans-serif;color:var(--text)}
.stage{position:relative;width:1122px;height:835px;transform:scale(1.06952);transform-origin:0 0;background:var(--page-bg)}
.abs{position:absolute}

.topbar{left:0;top:0;width:1122px;height:43px;background:linear-gradient(var(--bar-blue),var(--bar-blue-dark));border-bottom:1px solid #2f477a}
.site-mark{left:75px;top:9px;height:24px;display:flex;align-items:center;gap:5px;color:#fff;font-size:13px;font-weight:700}
.site-mark i{display:block;width:10px;height:10px;background:#fff;border-radius:2px}
.search{left:137px;top:9px;width:368px;height:24px;background:#fff;border-radius:2px;font-size:14px;color:#6a6f78;padding:4px 8px;display:flex;justify-content:space-between;align-items:center}
.search svg{width:14px;height:14px}

.notice{left:0;top:43px;width:1122px;height:27px;background:var(--notice-blue);color:#e7ebf3;font-size:12px;text-align:center;line-height:27px}
.notice b{color:#fff}

.admin-nav{left:75px;top:70px;width:984px;height:45px;background:var(--card);border:1px solid var(--card-line);border-top:0;border-radius:0 0 3px 3px;font-size:14px;color:var(--muted)}
.admin-nav span{position:absolute;top:15px}
.admin-nav .current{font-weight:700;color:var(--text)}
.admin-nav .current::after{content:"";position:absolute;left:-4px;right:-4px;top:26px;height:3px;background:var(--button-blue)}
.admin-nav .sep{top:0;width:1px;height:44px;background:var(--card-line)}

.cover{left:75px;top:124px;width:850px;height:314px;background:linear-gradient(100deg,#8fa3a8 0%,#a9b6b4 35%,#b9c1bb 60%,#8d9a90 100%);overflow:hidden}
.cover-shade{left:0;top:200px;width:850px;height:114px;background:linear-gradient(rgba(0,0,0,0),rgba(0,0,0,.45))}
.cover-line{left:0;width:850px;text-align:center;font-family:'Fira Sans',Arial,sans-serif;font-style:italic;font-weight:700;font-size:32px;color:var(--cover-text);padding-left:0}
.page-name{left:270px;top:370px;color:#fff;font-size:23px;font-weight:700;letter-spacing:.5px}
.page-tagline{left:270px;top:403px;color:#fff;font-size:17px}

.btn{height:28px;background:#f6f7f9;border:1px solid #cdd0d6;border-radius:2px;font-size:12px;font-weight:700;color:var(--muted);display:flex;align-items:center;justify-content:center;gap:5px}
.btn svg{width:13px;height:13px}

.profile{left:89px;top:300px;width:170px;height:169px;background:#fff;border:1px solid #c4c7cc;border-radius:3px;padding:4px}
.profile-inner{width:100%;height:100%;background:var(--brand-teal);display:flex;align-items:center;justify-content:center;color:#dfe7e8;font-size:26px;font-weight:400}

.page-tabs{left:75px;top:438px;width:850px;height:44px;background:var(--card);border:1px solid var(--card-line);border-top:0;font-size:14px;color:var(--muted)}
.page-tabs span{position:absolute;top:15px}
.page-tabs .current{font-weight:700;color:var(--text)}
.page-tabs .current::after{content:"";position:absolute;left:-3px;right:-3px;top:25px;height:3px;background:var(--button-blue)}
.page-tabs .sep{top:0;width:1px;height:43px;background:var(--card-line)}

.stats{left:937px;top:125px;width:122px;height:291px;background:var(--card);border:1px solid var(--card-line);border-radius:3px;text-align:center;overflow:hidden}
.stats h4{height:37px;line-height:37px;font-size:12px;background:var(--soft);border-bottom:1px solid var(--card-line)}
.stats h4.gap{border-top:1px solid var(--card-line)}
.stat{height:54px;padding-top:15px;font-size:13px;font-weight:700;margin:0 12px}
.stat+.stat{border-top:1px solid var(--card-line)}
.stat small{display:block;font-size:11px;font-weight:400;color:var(--link);margin-top:2px}

.years{left:937px;top:437px;width:100px;font-size:12px;color:var(--faint)}
.years div{height:24.5px;line-height:22px;padding-left:10px;border-left:3px solid #d2d5da}
.years .on{border-left-color:#6b7280;font-weight:700;color:#7a7f88}

.people{left:75px;top:493px;width:329px;height:313px;background:var(--card);border:1px solid var(--card-line);border-radius:3px}
.people-head{height:38px;background:var(--soft);border-bottom:1px solid var(--card-line);font-size:11px;font-weight:700;color:var(--muted);padding:13px 10px;display:flex;justify-content:space-between}
.likes-count{text-align:center;font-size:14px;color:var(--muted);height:44px;line-height:44px;border-bottom:1px solid var(--card-line)}
.likes-count b{color:var(--text);font-size:15px}
.friends-line{left:13px;top:96px;font-size:12px;color:var(--muted)}
.friends-line b{color:var(--link)}
.avatar{background:var(--avatar);overflow:hidden}
.avatar svg{width:100%;height:100%;display:block}
.more-friends{left:262px;top:121px;width:46px;height:46px;background:#e6eaf2;color:#7f92b8;font-size:18px;font-weight:700;display:flex;align-items:center;justify-content:center}
.person-name{font-size:12px;font-weight:700;color:var(--link)}
.invite{width:48px;height:24px;font-size:12px}
.see-all{left:13px;top:286px;font-size:12px;color:var(--link)}

.composer{left:415px;top:493px;width:510px;height:313px;background:var(--card);border:1px solid var(--card-line);border-radius:3px;overflow:hidden}
.composer-tabs{height:36px;border-bottom:1px solid var(--card-line);font-size:12px;font-weight:700;color:var(--text)}
.composer-tabs .tab{position:absolute;top:10px;display:flex;align-items:center;gap:7px}
.composer-tabs svg{width:15px;height:15px}
.notch{left:32px;top:29px;width:12px;height:12px;background:#fff;border-left:1px solid var(--card-line);border-top:1px solid var(--card-line);transform:rotate(45deg)}
.post-text{left:63px;top:49px;width:432px;height:218px;overflow:hidden;font-size:14px;line-height:18.2px;color:var(--text)}
.composer-foot{left:0;top:269px;width:510px;height:44px;background:var(--soft);border-top:1px solid var(--card-line)}
.composer-foot .tool{position:absolute;top:13px;width:17px;height:17px}
.boost{left:332px;top:9px;width:93px;height:25px}
.post-btn{left:441px;top:9px;width:61px;height:25px;background:var(--button-blue);border-color:#4563a0;color:#fff}
</style>
</head>
<body>
<div class="stage">

  <header class="abs topbar">
    <div class="abs site-mark"><i></i>Linkway</div>
    <div class="abs search"><span>Search for people, places and things</span>
      <svg viewBox="0 0 14 14"><circle cx="6" cy="6" r="4.2" fill="none" stroke="#9197a3" stroke-width="1.6"/><path d="M9 9l3.5 3.5" stroke="#9197a3" stroke-width="1.8"/></svg>
    </div>
  </header>

  <div class="abs notice">You are posting, commenting and liking as <b>Your Page Name</b> — Change to Personal Profile</div>

  <nav class="abs admin-nav">
    <span class="current" style="left:17px">Page</span>
    <i class="abs sep" style="left:67px"></i>
    <span style="left:84px">Activity</span>
    <i class="abs sep" style="left:145px"></i>
    <span style="left:162px">Insights</span>
    <i class="abs sep" style="left:228px"></i>
    <span style="left:245px">Settings</span>
    <span style="left:781px">Build Audience <small>▾</small></span>
    <i class="abs sep" style="left:906px"></i>
    <span style="left:923px">Help <small>▾</small></span>
  </nav>

  <section class="abs cover" role="img" aria-label="Cover photo: a child sitting on a hilltop working on a laptop, with falling columns of binary digits over a misty landscape">
    <div class="abs cover-shade"></div>
    <div class="abs cover-line" style="top:40px;left:-10px">bring your&nbsp; child</div>
    <div class="abs cover-line" style="top:83px;left:-1px">to learn the language</div>
    <div class="abs cover-line" style="top:126px;left:-5px">of the future</div>
  </section>
  <div class="abs page-name">BRIGHTVALE</div>
  <div class="abs page-tagline">Kid developing games and app</div>

  <div class="abs btn" style="left:600px;top:399px;width:84px">
    <svg viewBox="0 0 13 13"><path d="M1 6h3v6H1zM5 6l3-5c1 0 1.5.6 1.3 1.8L9 5h3c.7 0 1 .5.9 1.1l-1 5c-.1.5-.5.9-1 .9H5z" fill="#4e69a2"/></svg>Liked ▾</div>
  <div class="abs btn" style="left:695px;top:399px;width:90px">
    <svg viewBox="0 0 13 13"><path d="M1.5 7l3.5 3.5L11.5 3" fill="none" stroke="#4b4f56" stroke-width="2"/></svg>Following</div>
  <div class="abs btn" style="left:784px;top:399px;width:89px">
    <svg viewBox="0 0 13 13"><path d="M1 2h11v7H6l-3 3V9H1z" fill="#4b4f56"/></svg>Message</div>
  <div class="abs btn" style="left:872px;top:399px;width:53px;font-size:16px;letter-spacing:1px">•••</div>

  <div class="abs profile"><div class="profile-inner">Brightvale</div></div>

  <nav class="abs page-tabs">
    <span class="current" style="left:201px">Timeline</span>
    <i class="abs sep" style="left:276px"></i>
    <span style="left:292px">About</span>
    <i class="abs sep" style="left:346px"></i>
    <span style="left:362px">Photos</span>
    <i class="abs sep" style="left:423px"></i>
    <span style="left:439px">Likes</span>
    <i class="abs sep" style="left:489px"></i>
    <span style="left:505px">More <small>▾</small></span>
  </nav>

  <aside class="abs stats">
    <h4>THIS WEEK</h4>
    <div class="stat">999<small>Page Likes</small></div>
    <div class="stat">999<small>Post Reach</small></div>
    <h4 class="gap">UNREAD</h4>
    <div class="stat">999<small>Notifications</small></div>
    <div class="stat">999<small>Messages</small></div>
  </aside>

  <div class="abs years">
    <div class="on">Recent</div><div>2013</div><div>2012</div><div>2011</div><div>2010</div>
  </div>

  <section class="abs people">
    <div class="people-head"><span>PEOPLE</span>
      <svg width="10" height="12" viewBox="0 0 10 12"><path d="M2 1l5 5-5 5" fill="none" stroke="#4b4f56" stroke-width="2"/></svg></div>
    <div class="likes-count"><b>999</b> likes</div>
    <div class="abs friends-line"><b>Example person</b>, and <b>99 others</b> like this.</div>

    <div class="abs avatar" style="left:12px;top:121px;width:46px;height:46px"><svg viewBox="0 0 46 46"><circle cx="23" cy="17" r="9" fill="#fff"/><path d="M5 46c1-12 8-17 18-17s17 5 18 17z" fill="#fff"/></svg></div>
    <div class="abs avatar" style="left:62px;top:121px;width:46px;height:46px"><svg viewBox="0 0 46 46"><circle cx="23" cy="17" r="9" fill="#fff"/><path d="M5 46c1-12 8-17 18-17s17 5 18 17z" fill="#fff"/></svg></div>
    <div class="abs avatar" style="left:112px;top:121px;width:46px;height:46px"><svg viewBox="0 0 46 46"><circle cx="23" cy="17" r="9" fill="#fff"/><path d="M5 46c1-12 8-17 18-17s17 5 18 17z" fill="#fff"/></svg></div>
    <div class="abs avatar" style="left:162px;top:121px;width:46px;height:46px"><svg viewBox="0 0 46 46"><circle cx="23" cy="17" r="9" fill="#fff"/><path d="M5 46c1-12 8-17 18-17s17 5 18 17z" fill="#fff"/></svg></div>
    <div class="abs avatar" style="left:212px;top:121px;width:46px;height:46px"><svg viewBox="0 0 46 46"><circle cx="23" cy="17" r="9" fill="#fff"/><path d="M5 46c1-12 8-17 18-17s17 5 18 17z" fill="#fff"/></svg></div>
    <div class="abs more-friends">+99</div>

    <div class="abs avatar" style="left:12px;top:178px;width:40px;height:40px"><svg viewBox="0 0 46 46"><circle cx="23" cy="17" r="9" fill="#fff"/><path d="M5 46c1-12 8-17 18-17s17 5 18 17z" fill="#fff"/></svg></div>
    <div class="abs person-name" style="left:60px;top:192px">Example person</div>
    <div class="abs btn invite" style="left:267px;top:187px">Invite</div>

    <div class="abs avatar" style="left:12px;top:229px;width:40px;height:40px"><svg viewBox="0 0 46 46"><circle cx="23" cy="17" r="9" fill="#fff"/><path d="M5 46c1-12 8-17 18-17s17 5 18 17z" fill="#fff"/></svg></div>
    <div class="abs person-name" style="left:60px;top:243px">Example person</div>
    <div class="abs btn invite" style="left:267px;top:238px">Invite</div>

    <div class="abs see-all">See All Friends</div>
  </section>

  <section class="abs composer">
    <div class="composer-tabs">
      <div class="tab" style="left:11px"><svg viewBox="0 0 15 15"><rect width="15" height="15" rx="2" fill="#4e69a2"/><path d="M4 11l1-3 5-5 2 2-5 5z" fill="#fff"/></svg>Status</div>
      <div class="tab" style="left:90px"><svg viewBox="0 0 15 15"><rect x=".5" y=".5" width="14" height="14" rx="2" fill="#fde7d6" stroke="#e8873b"/><rect x="3" y="3" width="9" height="9" fill="#f2a466"/></svg>Photo / Video</div>
      <div class="tab" style="left:206px"><svg viewBox="0 0 15 15"><rect x=".5" y="1.5" width="14" height="13" fill="#fff" stroke="#555"/><rect x=".5" y="1.5" width="14" height="3" fill="#555"/><text x="7.5" y="12.5" font-size="7" text-anchor="middle" fill="#333" font-family="Arial">31</text></svg>Event, Milestone +</div>
    </div>
    <div class="abs notch"></div>
    <div class="abs avatar" style="left:11px;top:49px;width:41px;height:41px"><svg viewBox="0 0 46 46"><circle cx="23" cy="17" r="9" fill="#fff"/><path d="M5 46c1-12 8-17 18-17s17 5 18 17z" fill="#fff"/></svg></div>
    <p class="abs post-text">Lorem ipsum dolor sit amet, consectetur adipiscing elit. Etiam sit amet ante nisi, sit amet fermentum erat. Suspendisse vel nunc a massa consequat iaculis. Sed pellentesque vehicula elit. Mauris sodales mollis molestie. Integer ultrices laoreet ante, et faucibus sem cursus non. Suspendisse laoreet suscipit vestibulum. Integer mi augue, hendrerit ut fermentum ut, accumsan eget justo. Nam fringilla dapibus risus sed consequat. Nullam lacus urna, pellentesque et laoreet sit amet, volutpat sit amet dolor. Praesent a ultrices velit. Nulla facilisi. Ut sagittis dapibus bibendum. Proin id enim eros. Curabitur tincidunt lorem sed purus semper vitae tincidunt purus aliquet. Integer nulla metus, vestibulum at tincidunt at, euismod sed ligula. Vestibulum ante ipsum primis in faucibus orci luctus et ultrices posuere cubilia curae.</p>
    <div class="abs composer-foot">
      <svg class="tool" style="left:11px" viewBox="0 0 17 17"><circle cx="8.5" cy="8.5" r="7" fill="none" stroke="#8d949e" stroke-width="1.8"/><path d="M8.5 4.5v4.5h3" fill="none" stroke="#8d949e" stroke-width="1.8"/></svg>
      <svg class="tool" style="left:51px" viewBox="0 0 17 17"><path d="M8.5 1a5 5 0 015 5c0 4-5 10-5 10S3.5 10 3.5 6a5 5 0 015-5z" fill="#8d949e"/><circle cx="8.5" cy="6" r="2" fill="#f6f7f9"/></svg>
      <svg class="tool" style="left:91px" viewBox="0 0 17 17"><path d="M1 5h4l1.5-2h4L12 5h4v10H1z" fill="#8d949e"/><circle cx="8.5" cy="9.5" r="3" fill="#f6f7f9"/></svg>
      <div class="abs btn boost">Boost Post ▾</div>
      <div class="abs btn post-btn">Post</div>
    </div>
  </section>

</div>
</body>
</html>
```